Vorin Co Premium Matcha brand Label

This is a label design project for a luxury tea brand. Feel free to be creative within the guidelines.
Attached to this project is a document called “Private Label Design Requirements” with the design guidelines and template. There is another document called "Vorin Co Packaging Instructions" this has more details necessary to stick to the guidelines in the first document.

I have also attached the certifications to be included as well as different variations of the logo for you to use.

If you have any questions, I am here.

Need extra days to review

Young, active, fun, enjoy the finer things

```html
<!DOCTYPE html>
<html lang="en">
<head>
<meta charset="utf-8">
<title>Vorin Co Premium Matcha Labels</title>
<link rel="stylesheet" href="https://fonts.googleapis.com/css2?family=Barlow+Semi+Condensed:wght@400;500;600;700&family=Oswald:wght@500;600&display=swap">
<style>
  :root {
    --page: #ffffff;
    --sheet: #e6e7e8;
    --forest: #0f5a2c;
    --forest-deep: #083a1c;
    --leaf: #1f8a3d;
    --leaf-bright: #22a24a;
    --lime: #c8dc6a;
    --lime-bright: #8dc63f;
    --cream: #e2ecaf;
    --cream-deep: #d5e39a;
    --ink: #14361f;
    --white: #ffffff;
    --badge: #f2f5e6;
  }
  * { box-sizing: border-box; margin: 0; padding: 0; }
  html, body { width: 1200px; height: 783px; overflow: hidden; background: var(--page); }
  body { position: relative; font-family: "Barlow Semi Condensed", "Arial Narrow", sans-serif; }
  .sheet { position: absolute; left: 52px; top: 57px; width: 1096px; height: 688px; background: var(--sheet); }
  .label { position: absolute; left: 86px; width: 1026px; overflow: hidden; }
  .label--dark { top: 97px; height: 186px; background: radial-gradient(ellipse 60% 120% at 50% 40%, var(--leaf-bright) 0%, var(--leaf) 35%, var(--forest) 75%, var(--forest-deep) 100%); }
  .label--band { top: 321px; height: 170px; background: var(--cream); }
  .label--light { top: 531px; height: 170px; background: var(--cream); }
  .abs { position: absolute; }

  .brand { position: absolute; display: flex; align-items: center; gap: 7px; font-weight: 600; white-space: nowrap; }
  .brand__dot { border-radius: 50%; flex: none; }
  .brand--small { font-size: 17px; }
  .brand--small .brand__dot { width: 14px; height: 14px; }
  .brand--large { font-size: 26px; }
  .brand--large .brand__dot { width: 22px; height: 22px; }

  .origin { position: absolute; left: 47px; font-size: 14px; line-height: 17px; }
  .origin strong { font-weight: 600; display: block; }

  .details { position: absolute; font-size: 13.5px; line-height: 16px; }
  .details h3 { font-size: 13px; font-weight: 600; }
  .details ul { list-style: none; }
  .details li::before { content: "· "; }
  .details--indent li { padding-left: 8px; }
  .certs { display: flex; align-items: center; gap: 6px; margin-top: 7px; }
  .cert { width: 33px; height: 30px; background: var(--badge); border-radius: 3px; }
  .cert--round { width: 30px; border-radius: 50%; }
  .certs p { margin-left: 8px; font-size: 13px; font-weight: 600; line-height: 16px; }

  .pattern { position: absolute; top: 0; height: 100%; background: linear-gradient(135deg, var(--cream) 0%, var(--cream-deep) 50%, var(--cream) 100%); }

  .wordmark { position: absolute; font-family: "Oswald", "Arial Narrow", sans-serif; font-weight: 600; white-space: nowrap; letter-spacing: 0; }

  /* label 1 */
  .label--dark { color: var(--white); }
  .label--dark .brand__dot { background: var(--white); }
  .dark-title { position: absolute; left: 0; width: 1026px; text-align: center; font-weight: 600; }

  /* label 2 */
  .side { position: absolute; top: 0; height: 100%; background: var(--leaf); color: var(--white); }
  .side .brand__dot { background: var(--white); }
  .tag { position: absolute; background: var(--leaf); color: var(--white); font-weight: 600; font-size: 15px; line-height: 19px; padding: 3px 10px; }

  /* label 3 */
  .label--light { color: var(--ink); }
  .label--light .brand__dot { background: var(--ink); }
  .panel { position: absolute; left: 332px; top: 0; width: 282px; height: 170px; background: var(--leaf); overflow: hidden; }
  .panel__band { position: absolute; left: 130px; top: 88px; width: 152px; height: 48px; background: var(--cream); color: var(--ink); font-weight: 600; font-size: 15px; line-height: 19px; padding: 5px 13px; }
</style>
</head>
<body>
<div class="sheet"></div>

<!-- Label 1: dark gradient -->
<section class="label label--dark">
  <div class="brand brand--small" style="left:47px;top:70px;"><span class="brand__dot"></span>Vorin Co</div>
  <div class="origin" style="top:99px;"><strong>Product of Japan</strong>Distributed by Vorin Co | Atlanta, Ga<br>Certified Organic by Verdis</div>

  <div class="brand brand--large" style="left:462px;top:82px;"><span class="brand__dot"></span>Vorin Co</div>
  <p class="dark-title" style="top:124px;font-size:18px;color:var(--lime);">Premium Organic Ceremonial Matcha</p>
  <p class="dark-title" style="top:147px;font-size:14px;">Net Wt: 30g</p>

  <div class="details" style="left:780px;top:25px;">
    <h3>Premium Organic Japanese Matcha Green Tea</h3>
    <p>Instructions:</p>
    <ul>
      <li>2 tsp of Matcha</li>
      <li>2oz of Water (170-180 degrees F)</li>
      <li>Whisk in a W formation until frothy</li>
      <li>Sweeten to taste</li>
    </ul>
    <div class="certs"><span class="cert"></span><span class="cert cert--round"></span><p>KEEP REFRIGERATED<br>FOR QUALITY</p></div>
  </div>
</section>

<!-- Label 2: green ends, patterned middle -->
<section class="label label--band">
  <div class="side" style="left:0;width:249px;">
    <div class="brand brand--small" style="left:47px;top:66px;"><span class="brand__dot"></span>Vorin Co</div>
    <div class="origin" style="top:101px;"><strong>Product of Japan</strong>Distributed by Vorin Co | Atlanta, Ga<br>Certified Organic by Verdis</div>
  </div>
  <div class="pattern" role="img" aria-label="Tea leaf pattern" style="left:249px;width:185px;"></div>
  <div class="pattern" role="img" aria-label="Tea leaf pattern" style="left:582px;width:170px;"></div>

  <div class="brand" style="left:442px;top:22px;font-size:14px;color:var(--leaf);"><span class="brand__dot" style="width:11px;height:11px;background:var(--leaf);"></span>Vorin Co</div>
  <p class="wordmark" style="left:440px;top:52px;font-size:33px;line-height:44px;color:var(--leaf);">VORIN CO</p>
  <p class="tag" style="left:434px;top:100px;width:143px;">Premium Organic<br>Ceremonial Matcha</p>
  <p class="abs" style="left:446px;top:145px;font-size:12px;font-weight:600;color:var(--ink);">Net Wt: 30g</p>

  <div class="side" style="left:752px;width:274px;">
    <div class="details details--indent" style="left:26px;top:23px;">
      <h3>Premium Organic Japanese Matcha Green Tea</h3>
      <p>Instructions:</p>
      <ul>
        <li>2 tsp of Matcha</li>
        <li>2oz of Water (170-180 degrees F)</li>
        <li>Whisk in a W formation until frothy</li>
        <li>Sweeten to taste</li>
      </ul>
      <div class="certs"><span class="cert"></span><span class="cert cert--round"></span><p>KEEP REFRIGERATED<br>FOR QUALITY</p></div>
    </div>
  </div>
</section>

<!-- Label 3: light with central panel -->
<section class="label label--light">
  <div class="brand brand--small" style="left:47px;top:50px;"><span class="brand__dot"></span>Vorin Co</div>
  <div class="origin" style="top:100px;"><strong>Product of Japan</strong>Distributed by Vorin Co | Atlanta, Ga<br>Certified Organic by Verdis</div>

  <div class="pattern" role="img" aria-label="Tea leaf pattern" style="left:244px;width:88px;"></div>
  <div class="pattern" role="img" aria-label="Tea leaf pattern" style="left:614px;width:106px;"></div>

  <div class="panel">
    <div class="brand" style="left:22px;top:104px;font-size:18px;color:var(--ink);"><span class="brand__dot" style="width:14px;height:14px;background:var(--ink);"></span>Vorin Co</div>
    <p class="wordmark" style="right:16px;top:40px;font-size:31px;line-height:42px;color:var(--lime-bright);">VORIN CO</p>
    <p class="panel__band">Premium Organic<br>Ceremonial Matcha</p>
    <p class="abs" style="left:143px;top:144px;font-size:12px;font-weight:600;color:var(--white);">Net Wt: 30g</p>
  </div>

  <div class="details details--indent" style="left:778px;top:23px;">
    <h3>Premium Organic Japanese Matcha Green Tea</h3>
    <p>Instructions:</p>
    <ul>
      <li>2 tsp of Matcha</li>
      <li>2oz of Water (170-180 degrees F)</li>
      <li>Whisk in a W formation until frothy</li>
      <li>Sweeten to taste</li>
    </ul>
    <div class="certs"><span class="cert" style="background:var(--leaf);"></span><span class="cert cert--round" style="background:var(--white);"></span><p>KEEP REFRIGERATED<br>FOR QUALITY</p></div>
  </div>
</section>
</body>
</html>
```